Meridian Vessel, Inc. - Travel Worldwide
New Biz Cards for Modern Female Run Travel Agency - Travel
New Biz Cards for Modern Female Run Travel Agency
Simple
Loretta Pim, CTC
Owner
Boston, NY, Worldwide
loretta@meridianvessel-example.com
www.meridianvessel-example.com
We will need the same designed biz card for 2 main employees: Loretta Pim, CTC (Owner) loretta@meridianvessel-example.com Tamsin Ulwick, CTA (International Travel Consultant and Lead Planner) tamsin@meridianvessel-example.com
Honeymoons Destination Weddings Luxury Leisure Travel Your personal travel concierge.
MeridianVessel MeridianVessel
Hi plumquarto, thanks for all your submissions. we are reviewing and determining what we like and don't like. FYI what we like: 2 sided designs, clean lines, gray shading what we don't like: 1 sided designs, color fading, swirls/curves, duplicating designs on both sides, overuse of the logo THANK YOU
Hi Gondy, thanks for your submissions. a bit of text that we wanted to be included is missing, however. if you want to resubmit with that text, we have updated it to be: "Luxury Leisure Travel Honeymoons Destination Events Personal Travel Concierge"

```html
<!DOCTYPE html>
<html lang="en">
<head>
<meta charset="utf-8">
<title>Meridian Vessel, Inc. – Business Cards</title>
<link rel="stylesheet" href="https://fonts.googleapis.com/css2?family=Montserrat:wght@300;400;500&display=swap">
<style>
  :root {
    --backdrop: #e7e6e3;
    --card-white: #ffffff;
    --card-black: #141414;
    --ink-dark: #3a3a3a;
    --ink-grey: #8a8a8a;
    --ink-light: #f2f2f2;
    --ink-muted: #b9b9b9;
    --shadow: rgba(0, 0, 0, 0.18);
  }
  * { margin: 0; padding: 0; box-sizing: border-box; }
  html, body {
    width: 1200px; height: 899px; overflow: hidden;
    background: var(--backdrop);
    font-family: "Montserrat", sans-serif;
  }
  .stage {
    position: relative; width: 1200px; height: 899px;
    display: flex; flex-direction: column; align-items: center; justify-content: center; gap: 60px;
  }
  .card {
    width: 600px; height: 343px; border-radius: 26px; overflow: hidden;
    box-shadow: 0 14px 30px var(--shadow);
    display: flex;
  }
  .card__half { flex: 1; display: flex; flex-direction: column; justify-content: center; }
  .card__half--brand { background: var(--card-white); align-items: center; }
  .card__half--contact { background: var(--card-black); color: var(--ink-light); padding: 0 40px; }
  .card--back { background: var(--card-white); align-items: center; justify-content: center; flex-direction: column; }

  .brand { display: flex; flex-direction: column; align-items: center; gap: 14px; }
  .brand__mark { width: 46px; height: 46px; border: 1px solid var(--ink-grey); border-radius: 50%; }
  .brand__name {
    font-weight: 300; font-size: 17px; letter-spacing: 5px; text-transform: uppercase; color: var(--ink-dark);
  }
  .brand__tagline {
    font-weight: 300; font-size: 8px; letter-spacing: 4px; text-transform: uppercase; color: var(--ink-grey);
    margin-top: -6px;
  }
  .card--back .brand__mark { width: 56px; height: 56px; }
  .card--back .brand__name { font-size: 21px; letter-spacing: 6px; }
  .card--back .brand__tagline { font-size: 9px; }

  .person__name { font-weight: 400; font-size: 15px; letter-spacing: 2px; text-transform: uppercase; }
  .person__title { font-weight: 300; font-size: 10px; letter-spacing: 1.5px; color: var(--ink-muted); margin-top: 4px; }
  .contact-list { list-style: none; margin-top: 34px; display: flex; flex-direction: column; gap: 10px; }
  .contact-list__item { display: flex; align-items: center; gap: 10px; font-weight: 300; font-size: 10px; letter-spacing: 0.5px; }
  .contact-list__icon { width: 12px; height: 12px; flex: none; }
</style>
</head>
<body>
<main class="stage">
  <section class="card card--front">
    <div class="card__half card__half--brand">
      <div class="brand">
        <span class="brand__mark"></span>
        <span class="brand__name">Meridian Vessel</span>
        <span class="brand__tagline">Travel Worldwide</span>
      </div>
    </div>
    <div class="card__half card__half--contact">
      <p class="person__name">Loretta Pim, CTC</p>
      <p class="person__title">Owner</p>
      <ul class="contact-list">
        <li class="contact-list__item">
          <svg class="contact-list__icon" viewBox="0 0 12 12" fill="none" stroke="#f2f2f2" stroke-width="1"><path d="M3 1h2l1 3-1.5 1a6 6 0 0 0 2.5 2.5L8 6l3 1v2a1 1 0 0 1-1 1A9 9 0 0 1 2 2a1 1 0 0 1 1-1z"/></svg>
          +1 555 0101 4477
        </li>
        <li class="contact-list__item">
          <svg class="contact-list__icon" viewBox="0 0 12 12" fill="none" stroke="#f2f2f2" stroke-width="1"><rect x="1" y="2.5" width="10" height="7"/><path d="M1 2.5l5 4 5-4"/></svg>
          loretta@meridianvessel-example.com
        </li>
        <li class="contact-list__item">
          <svg class="contact-list__icon" viewBox="0 0 12 12" fill="none" stroke="#f2f2f2" stroke-width="1"><circle cx="6" cy="6" r="5"/><path d="M1 6h10M6 1c2 2 2 8 0 10M6 1c-2 2-2 8 0 10"/></svg>
          www.meridianvessel-example.com
        </li>
        <li class="contact-list__item">
          <svg class="contact-list__icon" viewBox="0 0 12 12" fill="none" stroke="#f2f2f2" stroke-width="1"><path d="M6 11s4-4 4-6.5a4 4 0 0 0-8 0C2 7 6 11 6 11z"/><circle cx="6" cy="4.5" r="1.3"/></svg>
          Boston, NY, Worldwide
        </li>
      </ul>
    </div>
  </section>

  <section class="card card--back">
    <div class="brand">
      <span class="brand__mark"></span>
      <span class="brand__name">Meridian Vessel</span>
      <span class="brand__tagline">Travel Worldwide</span>
    </div>
  </section>
</main>
</body>
</html>
```